Brightfern Development Corporation
Can I please see design #42 with the symbols to designate the Phone, Fax, Email and Address? Thanks.
I also like the back of the business card on design 43-45.
I like the cards that do not have too much red and over power the business card. I do like the symbols to designate phone, fax, email, address and the website information. I would like some color on the card though. I do not like the cards that are all white.
The logo should be uploaded now. Off to a good start, but please don't forget the stationary. We are looking for letterhead, envelopes, etc.

```html
<!DOCTYPE html>
<html lang="en">
<head>
<meta charset="utf-8">
<title>Brightfern Development Corporation — Stationery Set</title>
<link rel="stylesheet" href="https://fonts.googleapis.com/css2?family=Open+Sans:wght@400;700&display=swap">
<style>
  :root {
    --red: #e5412f;
    --red-deep: #c9301f;
    --charcoal: #3b3b3d;
    --grey: #8a8a8c;
    --paper: #ffffff;
    --stage: #ebebeb;
    --faint: #f6dcd8;
  }
  * { box-sizing: border-box; margin: 0; padding: 0; }
  html, body { width: 1200px; height: 302px; overflow: hidden; }
  body { background: var(--stage); font-family: "Open Sans", Arial, sans-serif; position: relative; color: var(--charcoal); }
  .piece { position: absolute; background: var(--paper); box-shadow: 0 1px 3px rgba(0,0,0,.18); overflow: hidden; }
  .piece svg { position: absolute; inset: 0; width: 100%; height: 100%; }

  .brand { position: absolute; display: flex; align-items: center; gap: 4px; font-weight: 700; color: var(--red); white-space: nowrap; }
  .brand .mark { background: var(--red); flex: none; }
  .brand.on-red { color: var(--paper); }
  .brand.on-red .mark { background: var(--paper); }

  .master-logo { left: 36px; top: 18px; }
  .master-logo .brand { position: static; font-size: 15px; }
  .master-logo .brand .mark { width: 12px; height: 12px; }
  .master-logo .tagline { font-size: 6px; color: var(--charcoal); letter-spacing: .5px; margin-top: 2px; text-transform: uppercase; }
  .master-logo .sub { font-size: 5px; color: var(--grey); margin-top: 2px; }
  .master-logo { position: absolute; }

  .card { width: 84px; height: 52px; }
  .card .brand { font-size: 6px; }
  .card .brand .mark { width: 5px; height: 5px; }
  .card .line { position: absolute; font-size: 3px; line-height: 4px; color: var(--charcoal); }
  .card.grey { background: #d9d9db; }
  .card.red { background: var(--red); }

  .letterhead { width: 220px; height: 274px; top: 14px; }
  .letterhead .brand { font-size: 9px; }
  .letterhead .brand .mark { width: 7px; height: 7px; }
  .letterhead .contact { position: absolute; font-size: 3.4px; line-height: 5px; color: var(--grey); }
  .letterhead .contact span::before { content: ""; display: inline-block; width: 3px; height: 3px; background: var(--red); margin-right: 2px; border-radius: 50%; }
  .letterhead .contact div { display: flex; align-items: center; }
  .letterhead .ghost { position: absolute; font-size: 24px; font-weight: 700; color: var(--faint); white-space: nowrap; }
  .letterhead .footer { position: absolute; bottom: 8px; left: 0; right: 0; text-align: center; font-size: 3px; color: var(--grey); }

  .envelope .brand { font-size: 6px; }
  .envelope .brand .mark { width: 5px; height: 5px; }
  .envelope .addr { position: absolute; font-size: 3px; line-height: 4px; color: var(--grey); }
</style>
</head>
<body>

  <div class="master-logo">
    <div class="brand"><span class="mark"></span>Brightfern</div>
    <div class="tagline">Development Corporation</div>
    <div class="sub">Building futures together</div>
  </div>

  <!-- business cards -->
  <div class="piece card" style="left:28px;top:108px;">
    <div class="brand" style="left:20px;top:20px;"><span class="mark"></span>Brightfern</div>
  </div>
  <div class="piece card" style="left:120px;top:108px;">
    <svg viewBox="0 0 84 52" preserveAspectRatio="none"><path d="M62 0 H84 V52 H70 Q56 26 62 0Z" fill="var(--red)"/></svg>
    <div class="line" style="left:6px;top:8px;font-weight:700;font-size:4px;">Jordan Ellery</div>
    <div class="line" style="left:6px;top:13px;">Project Director</div>
    <div class="line" style="left:6px;top:24px;">(555) 014-2280<br>(555) 014-2281<br>info@brightfern.example<br>48 Alder Row, Eastvale</div>
  </div>
  <div class="piece card grey" style="left:28px;top:228px;">
    <div class="brand" style="left:20px;top:20px;"><span class="mark"></span>Brightfern</div>
  </div>
  <div class="piece card red" style="left:120px;top:228px;">
    <svg viewBox="0 0 84 52" preserveAspectRatio="none"><path d="M0 0 H40 Q28 26 40 52 H0Z" fill="var(--paper)"/></svg>
    <div class="line" style="left:4px;top:10px;font-weight:700;font-size:4px;">Jordan Ellery</div>
    <div class="line" style="left:4px;top:22px;">(555) 014-2280<br>info@brightfern.example</div>
    <div class="brand on-red" style="left:48px;top:22px;"><span class="mark"></span>Brightfern</div>
  </div>

  <!-- letterhead with red band -->
  <div class="piece letterhead" style="left:216px;width:252px;">
    <svg viewBox="0 0 252 274" preserveAspectRatio="none">
      <path d="M0 0 H18 Q8 137 18 274 H0Z" fill="var(--red)"/>
      <path d="M18 0 Q8 137 18 274" stroke="var(--red-deep)" stroke-width="1" fill="none"/>
    </svg>
    <div class="brand" style="left:30px;top:12px;"><span class="mark"></span>Brightfern</div>
    <div class="contact" style="left:120px;top:10px;">
      <div><span></span>(555) 014-2280</div>
      <div><span></span>(555) 014-2281</div>
      <div><span></span>info@brightfern.example</div>
      <div><span></span>48 Alder Row, Eastvale</div>
    </div>
    <div class="ghost" style="left:62px;top:118px;">Brightfern</div>
    <div class="footer">www.brightfern.example</div>
  </div>

  <!-- plain letterhead -->
  <div class="piece letterhead" style="left:497px;width:204px;">
    <div class="brand" style="left:14px;top:12px;"><span class="mark"></span>Brightfern</div>
    <div class="contact" style="left:110px;top:10px;">
      <div><span></span>(555) 014-2280</div>
      <div><span></span>info@brightfern.example</div>
    </div>
    <div class="ghost" style="left:40px;top:118px;">Brightfern</div>
    <div class="footer">48 Alder Row, Eastvale · www.brightfern.example</div>
  </div>

  <!-- DL envelopes -->
  <div class="piece envelope" style="left:713px;top:96px;width:212px;height:68px;">
    <svg viewBox="0 0 212 68" preserveAspectRatio="none"><path d="M0 68 V58 Q106 48 212 60 V68Z" fill="var(--red)"/></svg>
    <div class="brand" style="left:8px;top:8px;"><span class="mark"></span>Brightfern</div>
    <div class="addr" style="left:8px;top:18px;">48 Alder Row, Eastvale</div>
  </div>
  <div class="piece envelope" style="left:713px;top:178px;width:212px;height:92px;">
    <svg viewBox="0 0 212 92" preserveAspectRatio="none"><path d="M0 0 H60 Q30 10 0 40Z" fill="var(--red)"/></svg>
    <div class="brand" style="left:70px;top:8px;"><span class="mark"></span>Brightfern</div>
    <div class="addr" style="left:70px;top:18px;">48 Alder Row, Eastvale</div>
  </div>

  <!-- envelope backs and fronts -->
  <div class="piece envelope" style="left:953px;top:36px;width:228px;height:72px;background:#dcdcde;">
    <svg viewBox="0 0 228 72" preserveAspectRatio="none"><path d="M0 0 L114 38 L228 0Z" fill="var(--charcoal)"/></svg>
    <div class="brand on-red" style="left:94px;top:10px;"><span class="mark"></span>Brightfern</div>
  </div>
  <div class="piece envelope" style="left:953px;top:112px;width:228px;height:72px;">
    <svg viewBox="0 0 228 72" preserveAspectRatio="none"><path d="M0 0 L114 36 L228 0Z" fill="var(--red)"/><path d="M0 72 L114 34 L228 72" stroke="#e2e2e2" fill="none"/></svg>
    <div class="brand on-red" style="left:94px;top:8px;"><span class="mark"></span>Brightfern</div>
  </div>
  <div class="piece envelope" style="left:953px;top:188px;width:228px;height:82px;">
    <svg viewBox="0 0 228 82" preserveAspectRatio="none"><path d="M0 0 L114 40 L228 0" stroke="#e2e2e2" fill="none"/><path d="M0 82 L114 38 L228 82" stroke="#e2e2e2" fill="none"/></svg>
  </div>

</body>
</html>
```